Luxury Brand Real Estate For Sale sign

**Update** I've added some examples from the internet of other signs that have a look similar to what I would like to see. I do not want my personal name in the sign. And the word FOR SALE Does not need to be so large - it can be more subtle.
I want to create a Real Estate for sale sign for my company that will be used for luxury/higher end real estate listings. I’m sharing my business card as well as a logo with new teal color to show what we're moving towards: we’re using Teal, white, black and gold.
Hoping the sign is simple, sophisticated and eye catching.
The sign should be 24" wide by 30" tall including the company name: Harbor Crest Realty Group and our logo, office phone number 727-555-0148 and website www.hcrgexample.com the words "For Sale"
Optional to add this e-mail address info@hcrgexample.com to the sign
Target Market(s)
Luxury home buyers
Industry/Entity Type
Real Estate
Look and feel

```html
<!DOCTYPE html>
<html lang="en">
<head>
<meta charset="utf-8">
<title>Harbor Crest Realty Group – For Sale Sign</title>
<link rel="stylesheet" href="https://fonts.googleapis.com/css2?family=Josefin+Sans:wght@300&family=Open+Sans:wght@600;700&display=swap">
<style>
  :root {
    --page: #ffffff;
    --teal: #0e827d;
    --teal-deep: #0b5f5d;
    --teal-light: #5cc2ba;
    --gold: #b38c1a;
    --white: #ffffff;
  }
  * { box-sizing: border-box; margin: 0; padding: 0; }
  html, body {
    width: 846px;
    height: 1200px;
    overflow: hidden;
    background: var(--page);
  }
  .canvas {
    position: relative;
    width: 846px;
    height: 1200px;
    background: var(--page);
  }
  .sign {
    position: absolute;
    left: 68px;
    top: 71px;
    width: 704px;
    height: 1053px;
    background: var(--teal);
    box-shadow: 6px 8px 10px rgba(0, 0, 0, 0.28);
    overflow: hidden;
  }
  .brand {
    position: absolute;
    left: 0;
    top: 28px;
    width: 100%;
    height: 145px;
    display: flex;
    flex-direction: column;
    align-items: center;
    justify-content: center;
    color: var(--white);
    font-family: "Josefin Sans", sans-serif;
    font-weight: 300;
    text-transform: uppercase;
    line-height: 1.1;
  }
  .brand__name { font-size: 50px; letter-spacing: 4px; }
  .brand__tag { font-size: 28px; letter-spacing: 9px; margin-top: 6px; }
  .status-band {
    position: absolute;
    left: 0;
    top: 203px;
    width: 100%;
    height: 153px;
    background: var(--gold);
    display: flex;
    align-items: center;
    justify-content: center;
  }
  .status-band__text {
    color: var(--white);
    font-family: "Open Sans", sans-serif;
    font-weight: 700;
    font-size: 104px;
    letter-spacing: 2px;
    line-height: 1;
  }
  .hero-photo {
    position: absolute;
    left: 0;
    top: 356px;
    width: 100%;
    height: 491px;
    background:
      linear-gradient(160deg, rgba(11, 95, 93, 0.9) 0%, rgba(92, 194, 186, 0.55) 45%, rgba(11, 95, 93, 0.95) 100%),
      linear-gradient(90deg, var(--teal-deep) 0%, var(--teal-light) 50%, var(--teal-deep) 100%);
  }
  .gold-rule {
    position: absolute;
    left: 0;
    top: 847px;
    width: 100%;
    height: 7px;
    background: var(--gold);
  }
  .contact {
    position: absolute;
    left: 0;
    width: 100%;
    display: flex;
    align-items: center;
    justify-content: center;
    gap: 10px;
    color: var(--white);
    font-family: "Open Sans", sans-serif;
    font-weight: 600;
    font-size: 52px;
    line-height: 1;
  }
  .contact--phone { top: 875px; }
  .contact--web { top: 953px; }
  .contact__icon { width: 40px; height: 40px; flex: none; }
</style>
</head>
<body>
  <div class="canvas">
    <div class="sign">
      <div class="brand">
        <span class="brand__name">Harbor Crest</span>
        <span class="brand__tag">Realty Group</span>
      </div>

      <div class="status-band">
        <span class="status-band__text">FOR SALE</span>
      </div>

      <div class="hero-photo" role="img" aria-label="Aerial view of a waterfront city with high-rise towers along a canal, tinted teal"></div>
      <div class="gold-rule"></div>

      <div class="contact contact--phone">
        <svg class="contact__icon" viewBox="0 0 24 24" fill="none" stroke="#ffffff" stroke-width="1.6" stroke-linejoin="round">
          <path d="M5 3h4l2 5-2.5 1.5a11 11 0 0 0 6 6L16 13l5 2v4a2 2 0 0 1-2 2A17 17 0 0 1 3 5a2 2 0 0 1 2-2z"/>
        </svg>
        <span>727-555-0148</span>
      </div>

      <div class="contact contact--web">
        <svg class="contact__icon" viewBox="0 0 24 24" fill="none" stroke="#ffffff" stroke-width="1.6" stroke-linejoin="round">
          <path d="M4 3l15 7-6 2 5 6-2.5 2-5-6L6 19z"/>
        </svg>
        <span>hcrgexample.com</span>
      </div>
    </div>
  </div>
</body>
</html>
```